Brochure Design: Text Messaging Service

We are looking for a brochure design for our new text messaging service. this should be a 2 page design on a 8.5x11" page
this should a clean design that catshed the eyey and features the features and benefits.
the brochure should bew designed so that we can entice our existing business clients to adopt this new service for their business.

Target Market(s)

business owner

Industry/Entity Type

Driving School

Font styles to use
Sans Serif

Colors
0692cd
33b8a4

Requirements
Must have
• pricing info, features, and screen shot on a computer. maybe also include image of your teen with cell phone.
Nice to have
• n/a
Should not have
• n/a

```html
<!DOCTYPE html>
<html lang="en">
<head>
<meta charset="utf-8">
<title>SMS Communication Module – LessonLink Software</title>
<link rel="stylesheet" href="https://fonts.googleapis.com/css2?family=Open+Sans:wght@300;400;600;700&family=Montserrat:wght@300;400;700&display=swap">
<style>
  :root {
    --brand-blue: #0b5aa6;
    --brand-sky: #0692cd;
    --brand-teal: #33b8a4;
    --ink: #555a60;
    --white: #ffffff;
    --page: #ffffff;
  }
  * { box-sizing: border-box; margin: 0; padding: 0; }
  html, body { width: 855px; height: 1200px; overflow: hidden; background: var(--page); }
  body { font-family: "Open Sans", Arial, sans-serif; color: var(--ink); position: relative; }

  .brand { position: absolute; left: 74px; top: 30px; width: 180px; text-align: center; }
  .brand-mark { width: 46px; height: 46px; border-radius: 50%; background: var(--brand-blue); margin: 0 auto 10px; }
  .brand-name { font-weight: 700; font-size: 22px; color: var(--brand-blue); letter-spacing: 0.2px; }
  .brand-tagline { font-size: 5.6px; font-weight: 700; color: var(--brand-blue); margin-top: 4px; letter-spacing: 0.2px; }

  .hero { position: absolute; left: 0; top: 156px; width: 855px; height: 528px; }
  .hero-photo { position: absolute; inset: 0;
    background: linear-gradient(90deg, #3a1e2a 0%, #6b3a3c 28%, #a8744e 48%, #5d3a2c 62%, #2e8bd0 78%, #d9a07c 100%); }
  .hero-copy { position: absolute; left: 39px; top: 82px; width: 420px; color: var(--white); }
  .hero-kicker { font-family: "Montserrat", Arial, sans-serif; font-weight: 300; font-size: 31px; line-height: 1; }
  .hero-title { font-family: "Montserrat", Arial, sans-serif; font-weight: 700; font-size: 44px; line-height: 1; margin-top: 4px; letter-spacing: -0.5px; }
  .hero-title-light { font-family: "Montserrat", Arial, sans-serif; font-weight: 300; font-size: 50px; line-height: 1; letter-spacing: 0.5px; }
  .hero-text { font-size: 18.4px; line-height: 25.2px; margin-top: 10px; }
  .hero-phone { position: absolute; left: 39px; top: 431px; width: 307px; height: 58px; background: var(--brand-blue);
    display: flex; align-items: center; justify-content: center; color: var(--white);
    font-weight: 700; font-size: 41px; letter-spacing: -0.5px; }

  .gallery-item { position: absolute; top: 713px; width: 237px; height: 148px; }
  .shot-devices { left: 41px; background: linear-gradient(180deg, #dcdcdc, #cfcfcf); }
  .shot-teens { left: 308px; background: linear-gradient(90deg, #c25a4a, #d9473a 35%, #e7c24a 60%, #6f8fb3 85%, #9aa8b8); }
  .shot-desk { left: 575px; background: linear-gradient(180deg, #f1f1f1, #d9dadb 70%, #8d8f92); }

  .column { position: absolute; top: 884px; font-size: 11.6px; line-height: 16.8px; font-weight: 400; }
  .column-intro { left: 39px; width: 240px; }
  .column-details { left: 308px; width: 245px; }
  .column-features { left: 575px; width: 250px; }
  .features-title { color: var(--brand-blue); font-weight: 700; font-size: 13px; line-height: 16.8px; }
  .features-list { list-style: none; margin-left: 9px; }
  .features-list li { position: relative; padding-left: 8px; }
  .features-list li::before { content: "*"; position: absolute; left: 0; top: -1px; color: var(--brand-sky); font-weight: 700; }

  .site-link { position: absolute; left: 228px; top: 1140px; width: 376px; height: 32px; background: var(--brand-blue);
    color: var(--white); display: flex; align-items: center; justify-content: center;
    font-size: 15px; font-weight: 600; letter-spacing: 1.4px;
    box-shadow: 0 10px 10px -6px rgba(0,0,0,0.45); }
</style>
</head>
<body>
  <header class="brand">
    <div class="brand-mark"></div>
    <div class="brand-name">LessonLink Software</div>
    <div class="brand-tagline">ENROLLMENT - BILLING - SCHEDULING - REPORTING AND MORE</div>
  </header>

  <section class="hero">
    <div class="hero-photo" role="img" aria-label="Smiling young woman in a blue top typing a text message on her smartphone, warm blurred interior behind"></div>
    <div class="hero-copy">
      <div class="hero-kicker">SMS</div>
      <div class="hero-title">COMMUNICATION</div>
      <div class="hero-title-light">MODULE</div>
      <p class="hero-text">The SMS Communication Module is designed to allow your school to effectively communicate with both parent and students in near real-time. In today’s world, both students and parent expect almost instant communication with the service provider and driving schools.</p>
    </div>
    <div class="hero-phone">555.014.2290</div>
  </section>

  <div class="gallery-item shot-devices" role="img" aria-label="Messaging dashboard shown on a desktop monitor, laptop, tablet and phone"></div>
  <div class="gallery-item shot-teens" role="img" aria-label="Group of teenagers in jeans leaning on a wall while using their phones"></div>
  <div class="gallery-item shot-desk" role="img" aria-label="Desktop computer on a white desk displaying the messaging dashboard"></div>

  <p class="column column-intro">With our integrated SMS Messaging Module, your school can automatically send reminders for classroom lessons, in-car lessons, road tests, urgent notifications and more. Students and parents can also reply to those messages. Each school will be assigned a dedicated phone number, which could be either local number of your choice or toll-free number. Because this module is fully integrated, the staff will not need to use any external or third-party services to accomplish the same effect, saving time and money.</p>

  <p class="column column-details">Each SMS phone number is tracked individually and assigned to a student account. During the enrollment process, students and parents can opt to receive SMS notifications. However, at any point later on, they can add or remove phone numbers for notifications. The SMS Communication Module is the first step in a very extensive list of features and capabilities that LessonLinkSoftware.com offers. With plans starting at $25/month, it is a very affordable solution for your school and business, while providing an efficient and cost effective communication tool.</p>

  <div class="column column-features">
    <h2 class="features-title">FEATURES:</h2>
    <ul class="features-list">
      <li>Dedicated local or toll-free phone number</li>
      <li>Custom message content</li>
      <li>Delivery confirmation</li>
      <li>Two-way messaging</li>
      <li>On-demand messaging</li>
      <li>Phone number validation</li>
      <li>Online enrollment integration</li>
      <li>Mass communication</li>
      <li>Plans starting at $25/month for 500 messages. Additional messages $0.03/message</li>
    </ul>
  </div>

  <div class="site-link">http://lessonlinksoftware.com/</div>
</body>
</html>
```